We need a brand logo for a range of health supplements we are launching.

The brand is called 'Quill Nest' The tagline for our brand is "The Entrepreneurs Supplement"

The brand is aimed at Entrepreneurs who would use our supplements to ultimately increase their brain power and turn them into more successful entrepreneurs.

As an additional note. The first product we launch is going to be a brain supplement that supports mental focus, promotes clarity and aids memory function. It's going to be called the Quill Nest Am Formula. This is a supplement which will be taken by entrepreneurs in the morning. The logo must therefore be suitable to incorporate it into the packaging design for our first product.

The product itself is a bottle of 60 capsules that comes in a box. (Therefore, it's a plastic bottle inside a cardboard box).

The bottle is black and comes with a black cap. I have attached an example of the bottle.

Also attached is the label template for the bottle. Everything that is displayed on the right and left hand side of the bottle must be visible. Everything in the middle can be deleted and re-designed except for 'Dietary supplement 60 Capsules' which must also be displayed.

Also attached is the box template. The box template is where all the creative design work should take place which can then be replicated onto the bottle.

The finished project should be a 3D render of the box and bottle side by side.

We would require the box and label templates to give to out manufacturer for printing.

Target Market(s)

Entrepreneurs

Industry/Entity Type

Health And Wellness

Logo Text

Quill Nest - The Entrepreneurs Supplement

Colors
3176b5
0255a3
85abd2
ffffff
e8e8e8
959595
f6f6f6
919191

Requirements
Must have
• This product must be aimed at entrepreneurs.
• The colur scheme should be Blue, Grey and White. The color schemes I have suggested

```html
<!DOCTYPE html>
<html lang="en">
<head>
<meta charset="utf-8">
<title>Quill Nest – The Entrepreneurs Supplement</title>
<link href="https://fonts.googleapis.com/css2?family=Montserrat:wght@700;800&family=Cinzel:wght@500;600&display=swap" rel="stylesheet">
<style>
  :root {
    --stage: #f6f6f6;
    --panel: #0c0c0d;
    --frame: #959595;
    --silver: #e8e8e8;
    --silver-mid: #bdbdbd;
    --silver-dark: #919191;
    --blue-deep: #0255a3;
    --blue: #3176b5;
    --blue-light: #85abd2;
    --white: #ffffff;
    --ink: #1a1a1a;
  }
  * { margin: 0; padding: 0; box-sizing: border-box; }
  html, body {
    width: 1200px; height: 960px; overflow: hidden;
    background: var(--stage);
  }
  .box-front {
    position: absolute; left: 300px; top: 30px;
    width: 600px; height: 900px;
    background: var(--panel);
  }
  .box-front__shapes { position: absolute; inset: 0; }
  .brand-name {
    position: absolute; left: 0; right: 0;
    text-align: center;
    font-family: "Montserrat", Arial, sans-serif;
    font-weight: 800;
    color: var(--silver);
    line-height: 1;
  }
  .brand-name--top { top: 110px; font-size: 118px; letter-spacing: 2px; }
  .brand-name--bottom { top: 255px; font-size: 168px; letter-spacing: 2px; }
  .tagline {
    position: absolute; left: 0; right: 0; top: 488px;
    text-align: center;
    font-family: "Cinzel", "Times New Roman", serif;
    font-weight: 600;
    font-size: 27px; line-height: 34px;
    color: var(--white);
    letter-spacing: 1px;
  }
  .claims {
    position: absolute; left: 0; right: 0; top: 686px;
    text-align: center;
    font-family: "Cinzel", "Times New Roman", serif;
    font-weight: 600;
    font-size: 26px; line-height: 33px;
    color: var(--ink);
    letter-spacing: 1px;
  }
  .product-info {
    position: absolute; left: 0; right: 0; top: 808px;
    text-align: center;
    font-family: "Montserrat", Arial, sans-serif;
    font-weight: 800;
    font-size: 32px; line-height: 42px;
    color: var(--silver);
  }
</style>
</head>
<body>
  <main class="box-front">
    <svg class="box-front__shapes" width="600" height="900" viewBox="0 0 600 900" aria-hidden="true">
      <defs>
        <radialGradient id="chevron-glow" cx="50%" cy="60%" r="60%">
          <stop offset="0" stop-color="var(--blue)"/>
          <stop offset="0.55" stop-color="var(--blue-deep)"/>
          <stop offset="1" stop-color="#0a1f3e"/>
        </radialGradient>
        <linearGradient id="band-silver" x1="0" y1="0" x2="1" y2="0">
          <stop offset="0" stop-color="var(--silver-dark)"/>
          <stop offset="0.15" stop-color="var(--silver)"/>
          <stop offset="0.5" stop-color="var(--white)"/>
          <stop offset="0.85" stop-color="var(--silver)"/>
          <stop offset="1" stop-color="var(--silver-dark)"/>
        </linearGradient>
      </defs>
      <path class="shield-frame" d="M40 0 V520 L300 640 L560 520 V0" fill="none" stroke="var(--frame)" stroke-width="5"/>
      <path class="shield-chevron" d="M54 470 H546 V520 L300 630 L54 520 Z" fill="url(#chevron-glow)" stroke="var(--silver-mid)" stroke-width="2"/>
      <rect class="claims-band" x="0" y="672" width="600" height="118" fill="url(#band-silver)"/>
    </svg>

    <h1 class="brand-name brand-name--top">QUILL</h1>
    <p class="brand-name brand-name--bottom">NEST</p>
    <p class="tagline">The Entrepreneurs<br>Supplement</p>
    <p class="claims">Supports Mental Focus*<br>Promotes Clarity*<br>Memory Function Aid*</p>
    <p class="product-info">Dietary Supplement<br>60 Capsules</p>
  </main>
</body>
</html>
```